Travel Company is looking for a STAND OUT Business Card

I need a unique Business Card that will truly stand out. Nothing too busy. Simple is good, right? Not looking for a standard design either. No cookie cutter layout. We are a Travel Company that works more with Companies than Travelers. I had an idea to focus and emphasis on the 2 logo a bit more. This is not necessary, however thought it would look interesting. I am just looking for something interesting and a bit different. Does't have to completely off the wall crazy, just not your run of the mill business card.

Target Market(s)

Hoteliers, Resort Management, Call Centers, Executives, Travelers, Families, Businesses

Industry/Entity Type

Hospitality

Contact Information for Business Card

President/CEO - Marcus T Bellamy (title not necessary if design doesn't allow for it)
contact - (407) 555-0186
email - mbellamy@wayfarenow.example
address - 4812 Quillmore Ave #164
Orlando, FL 32804
website - www.wayfarenow.example

Font styles to use
Serif
Other font styles liked:
• Avenir Next LT Pro BOLD

Requirements
Must have
• simple look and design. Unique design
Nice to have
• I attached the 2 logo separate from the main logo. This can be used separately from the Main Logo, together with the main logo or as main logo. I included the logo font. Use it or not, designers choice.
Should not have
• cookie cutter design. Little use of red other than the logo

```html
<!DOCTYPE html>
<html lang="en">
<head>
<meta charset="utf-8">
<title>wayfarenow business card</title>
<link rel="stylesheet" href="https://fonts.googleapis.com/css2?family=Lato:wght@700;900&display=swap">
<style>
  :root {
    --backdrop: #2b2b2b;
    --card: #f7f7f7;
    --ink: #1e1a1c;
    --brand-red: #d0021b;
    --card-shadow: rgba(0, 0, 0, 0.45);
  }
  * { margin: 0; padding: 0; box-sizing: border-box; }
  html, body {
    width: 1200px;
    height: 900px;
    overflow: hidden;
    background: var(--backdrop);
  }
  .canvas {
    position: relative;
    width: 1200px;
    height: 900px;
    font-family: "Lato", "Helvetica Neue", Arial, sans-serif;
    color: var(--ink);
  }
  .card {
    position: absolute;
    width: 600px;
    height: 343px;
    background: var(--card);
    box-shadow: 0 14px 32px var(--card-shadow);
    overflow: hidden;
  }
  .card--front { left: 70px; top: 90px; }
  .card--back { left: 530px; top: 467px; }

  /* front: brand name centred */
  .brand {
    position: absolute;
    inset: 0;
    display: flex;
    align-items: center;
    justify-content: center;
    gap: 14px;
  }
  .brand__dot {
    width: 34px;
    height: 34px;
    border-radius: 50%;
    background: var(--brand-red);
  }
  .brand__name {
    font-weight: 900;
    font-size: 52px;
    letter-spacing: -0.5px;
    color: var(--ink);
  }

  /* back: contact left, mark centre, address right */
  .contact, .address {
    position: absolute;
    font-weight: 700;
    font-size: 15px;
    line-height: 22px;
    white-space: nowrap;
  }
  .contact { right: 334px; top: 130px; text-align: right; }
  .address { left: 398px; top: 66px; text-align: left; }

  .mark {
    position: absolute;
    left: 276px;
    top: 80px;
    width: 112px;
    display: flex;
    flex-direction: column;
    align-items: center;
    gap: 10px;
  }
  .mark__dot {
    width: 100px;
    height: 100px;
    border-radius: 50%;
    background: var(--brand-red);
  }
  .mark__name {
    font-weight: 900;
    font-size: 17px;
    color: var(--ink);
  }
</style>
</head>
<body>
<main class="canvas">
  <section class="card card--front" aria-label="Card front">
    <div class="brand">
      <span class="brand__dot"></span>
      <span class="brand__name">wayfarenow</span>
    </div>
  </section>

  <section class="card card--back" aria-label="Card back">
    <div class="contact">
      <p class="contact__name">Marcus T Bellamy</p>
      <p class="contact__phone">(407) 555-0186</p>
      <p class="contact__email">mbellamy@wayfarenow.example</p>
    </div>
    <div class="mark">
      <span class="mark__dot"></span>
      <span class="mark__name">wayfarenow</span>
    </div>
    <div class="address">
      <p>4812 Quillmore Ave #164</p>
      <p>Orlando, FL 32804</p>
      <p>www.wayfarenow.example</p>
    </div>
  </section>
</main>
</body>
</html>
```